Dr. Marisa Tellen Medical/Chiropractic Business Card

Dr. Tellen is a chiropractor and will require a business card that she uses every single day to book appointments on the back side of the card. Currently the office name goes by Dr. Marisa Tellen. The chiropractic profession is based on the diagnosis and manipulative treatment of misalignments of the joints, especially those of the spinal column, which are held to cause other disorders by affecting the nerves, muscles, and organs. Dr. Marisa Tellen is looking for a contemporary and minimalistic design.

Industry/Entity Type

Medical

Contact Information for Business Card

Name: Dr. Marisa Tellen; Address: 748 Ashcombe Rd North, London, ON N5R 2K9; Phone Number: 519.672.4193; Fax: 519.681.2054; email: marisa.tellen@brevanmail.com

Requirements
Must have
• ability to write multiple appointments date/time on the back of card

```html
<!DOCTYPE html>
<html lang="en">
<head>
<meta charset="utf-8">
<title>Dr. Marisa Tellen – Chiropractor Business Card</title>
<link rel="stylesheet" href="https://fonts.googleapis.com/css2?family=Raleway:ital,wght@0,400;0,500;0,800;1,400&display=swap">
<style>
  :root {
    --page-bg: #e9e7e3;
    --card-bg: #ffffff;
    --brand-blue: #1a1ae6;
    --ink: #2b2b2b;
    --card-shadow: rgba(0, 0, 0, 0.18);
  }
  * { box-sizing: border-box; margin: 0; padding: 0; }
  html, body {
    width: 1200px;
    height: 960px;
    overflow: hidden;
    background: var(--page-bg);
    font-family: "Raleway", sans-serif;
  }
  .sheet {
    width: 1200px;
    height: 960px;
    display: flex;
    flex-direction: column;
    align-items: center;
    justify-content: center;
    gap: 56px;
  }
  .card {
    width: 680px;
    height: 389px;
    background: var(--card-bg);
    border-radius: 10px;
    box-shadow: 0 10px 28px var(--card-shadow);
    position: relative;
    overflow: hidden;
  }

  /* Front */
  .card-front .details {
    position: absolute;
    left: 190px;
    top: 78px;
    color: var(--ink);
  }
  .doctor-name {
    font-size: 40px;
    font-weight: 400;
    color: var(--brand-blue);
    letter-spacing: 0.3px;
    line-height: 1.05;
  }
  .doctor-title {
    font-size: 19px;
    font-weight: 500;
    margin-top: 4px;
    margin-left: 22px;
  }
  .address {
    font-size: 19px;
    font-weight: 500;
    line-height: 1.25;
    margin-top: 28px;
    margin-left: 48px;
    font-style: normal;
  }
  .contact-list {
    list-style: none;
    margin-top: 26px;
    margin-left: 82px;
  }
  .contact-list li {
    display: flex;
    align-items: center;
    gap: 10px;
    font-size: 19px;
    font-weight: 500;
    margin-bottom: 6px;
  }
  .contact-list li:nth-child(2) { margin-left: 18px; }
  .contact-list li:nth-child(3) { margin-left: 36px; }
  .contact-icon {
    width: 30px;
    height: 30px;
    flex: none;
  }

  /* Back */
  .card-back .heading {
    position: absolute;
    top: 36px;
    left: 0;
    right: 0;
    text-align: center;
    font-size: 32px;
    font-weight: 800;
    color: var(--brand-blue);
    letter-spacing: 1px;
    line-height: 1.2;
  }
  .schedule {
    position: absolute;
    left: 60px;
    right: 60px;
    top: 92px;
    display: grid;
    grid-template-columns: repeat(4, 1fr);
    grid-template-rows: 20px repeat(4, 22px);
    column-gap: 22px;
    row-gap: 18px;
  }
  .schedule .col-label {
    font-size: 17px;
    font-weight: 500;
    color: var(--ink);
    line-height: 20px;
    text-align: center;
  }
  .schedule .entry-line {
    border-bottom: 2px solid var(--brand-blue);
  }
  .card-back .notice {
    position: absolute;
    left: 0;
    right: 0;
    bottom: 30px;
    text-align: center;
    font-size: 17px;
    font-style: italic;
    color: var(--brand-blue);
    line-height: 1.3;
  }
</style>
</head>
<body>
<main class="sheet">

  <section class="card card-front" aria-label="Business card front">
    <div class="details">
      <h1 class="doctor-name">Dr. Marisa Tellen</h1>
      <p class="doctor-title">Chiropractor</p>
      <address class="address">748 Ashcombe Rd North<br>London, ON N5R 2K9</address>
      <ul class="contact-list">
        <li>
          <svg class="contact-icon" viewBox="0 0 30 30" aria-hidden="true">
            <circle cx="15" cy="15" r="15" fill="var(--brand-blue)"/>
            <path d="M10.5 8.5c.8-.6 1.7-.4 2.1.4l1.2 2.4c.3.7.1 1.3-.5 1.7l-.8.6c.7 1.6 1.9 2.9 3.5 3.6l.6-.8c.4-.6 1.1-.8 1.7-.5l2.4 1.2c.8.4 1 1.3.4 2.1l-.9 1c-.8.9-2.1 1.1-3.2.6-3.6-1.600-6.3-4.3-7.900-7.900-.5-1.1-.3-2.4.6-3.2z" fill="#fff"/>
          </svg>
          <span>519.672.4193</span>
        </li>
        <li>
          <svg class="contact-icon" viewBox="0 0 30 30" aria-hidden="true">
            <circle cx="15" cy="15" r="15" fill="var(--brand-blue)"/>
            <rect x="10" y="7" width="8" height="6" fill="#fff"/>
            <rect x="8" y="12" width="14" height="11" rx="1.5" fill="#fff"/>
            <rect x="10.5" y="15" width="6" height="1.6" fill="var(--brand-blue)"/>
            <rect x="10.5" y="18" width="6" height="1.6" fill="var(--brand-blue)"/>
            <rect x="18" y="15" width="2" height="4.6" fill="var(--brand-blue)"/>
          </svg>
          <span>Fax: 519.681.2054</span>
        </li>
        <li>
          <svg class="contact-icon" viewBox="0 0 30 30" aria-hidden="true">
            <circle cx="15" cy="15" r="15" fill="var(--brand-blue)"/>
            <rect x="7.5" y="10" width="15" height="10.5" rx="1" fill="#fff"/>
            <path d="M8 10.6l7 5.6 7-5.6" fill="none" stroke="var(--brand-blue)" stroke-width="1.4"/>
          </svg>
          <span>marisa.tellen@brevanmail.com</span>
        </li>
      </ul>
    </div>
  </section>

  <section class="card card-back" aria-label="Business card back">
    <h2 class="heading">APPOINTMENTS</h2>
    <div class="schedule">
      <span class="col-label">Date</span>
      <span class="col-label">Time</span>
      <span class="col-label">Date</span>
      <span class="col-label">Time</span>
      <span class="entry-line"></span><span class="entry-line"></span><span class="entry-line"></span><span class="entry-line"></span>
      <span class="entry-line"></span><span class="entry-line"></span><span class="entry-line"></span><span class="entry-line"></span>
      <span class="entry-line"></span><span class="entry-line"></span><span class="entry-line"></span><span class="entry-line"></span>
      <span class="entry-line"></span><span class="entry-line"></span><span class="entry-line"></span><span class="entry-line"></span>
    </div>
    <p class="notice">If you are unable to make your appointment,<br>please call us to reschedule</p>
  </section>

</main>
</body>
</html>
```